Designing a Chocolate Bar's Package

We are a chocolate manufacturing company located in Lebanon. We produce chocolate on a wholesale level, and we are planning a new line of production at the moment.
We intend to be make small chocolate bars (about 30g) similar to the "Varmo Radiance" bar with several flavors. 2 flavors have been decided so far (Mint flavored dark chocolate and Plain dark chocolate).
The packaging material will be similar to varmo's package as well. It won't be a carton box. It'll be some sort of paper wrapping the entire bar. So I am looking for a design that has a unique and cool front and back look.
If only one design is to be prepared, please choose either the mint's flavor or the plain dark chocolate, and prepare the design accordingly.
Updates
Project Deadline Extended
Reason: I still have some time to begin the production. The new deadline,therefore, is the end of this month.
Target Market(s)
basically all chocolate lovers...
Industry/Entity Type
It Company
Requirements
Must have
- I will be uploading our logo. Please make sure to use it in the design.

```html
<!DOCTYPE html>
<html lang="en">
<head>
<meta charset="utf-8">
<title>Corano – Chocolate Bar Wrapper, Back</title>
<link rel="stylesheet" href="https://fonts.googleapis.com/css2?family=Arimo:wght@400;700&display=swap">
<style>
  :root {
    --page-bg: #ffffff;
    --frame-dark: #2a160c;
    --frame-mid: #6b3f24;
    --frame-light: #d9c2ae;
    --panel-light: #f1f0ee;
    --panel-grey: #d6d6d6;
    --mint-haze: rgba(92, 128, 52, 0.55);
    --cocoa: #6a3818;
    --cocoa-deep: #3f1d0b;
    --cocoa-brand: #5a3219;
    --ink: #1d1d1d;
    --white: #ffffff;
    --bar-fill: rgba(240, 240, 236, 0.85);
  }
  * { box-sizing: border-box; margin: 0; padding: 0; }
  html, body {
    width: 1200px; height: 2275px; overflow: hidden;
    background: var(--page-bg);
    font-family: "Arimo", Arial, sans-serif;
  }
  .canvas { position: relative; width: 1200px; height: 2275px; }

  .wrapper-frame {
    position: absolute; left: 99px; top: 190px; width: 1003px; height: 1904px;
    background: linear-gradient(90deg, var(--frame-mid) 0%, var(--frame-dark) 3%, var(--frame-light) 5%, var(--frame-light) 95%, var(--frame-dark) 97%, var(--frame-mid) 100%);
    border-radius: 6px;
    box-shadow: inset 0 0 0 3px var(--frame-dark), 0 2px 6px rgba(0,0,0,0.35);
  }
  .wrapper-panel {
    position: absolute; left: 152px; top: 243px; width: 903px; height: 1803px;
    background:
      radial-gradient(ellipse 380px 260px at 560px 1040px, var(--mint-haze), transparent 70%),
      radial-gradient(ellipse 520px 120px at 470px 280px, rgba(120,150,80,0.25), transparent 70%),
      linear-gradient(180deg, var(--panel-light) 0%, var(--panel-grey) 60%, var(--panel-light) 100%);
    box-shadow: 0 0 18px 6px rgba(255,255,255,0.9);
  }

  .brand-name {
    position: absolute; left: 0; width: 1200px; top: 330px;
    text-align: center; font-size: 140px; font-weight: 400;
    color: var(--cocoa-brand); letter-spacing: 2px; line-height: 1;
  }

  .product-visual {
    position: absolute; left: 213px; top: 657px; width: 349px; height: 274px;
    border-radius: 10px;
    background: radial-gradient(ellipse at 40% 40%, #8a4a22 0%, var(--cocoa) 55%, var(--cocoa-deep) 100%);
    box-shadow: 0 0 8px 3px rgba(255,255,255,0.7);
  }

  .copy { position: absolute; color: var(--ink); }
  .copy-intro { left: 604px; top: 655px; width: 436px; font-size: 14.5px; line-height: 18.9px; }
  .copy-wide { left: 222px; top: 984px; width: 820px; font-size: 15.5px; line-height: 19px; }
  .copy-detail { left: 616px; top: 1228px; width: 428px; font-size: 19.5px; line-height: 26.6px; }

  .nutrition-panel {
    position: absolute; left: 228px; top: 1231px; width: 352px; height: 646px;
    border: 2px solid var(--white);
  }
  .nutrition-title {
    position: absolute; left: 0; width: 100%; top: 12px;
    text-align: center; color: var(--white); font-size: 28px;
  }
  .nutrition-rule { position: absolute; left: 20px; width: 312px; top: 55px; height: 3px; background: var(--white); }
  .nutrition-divider { position: absolute; left: 174px; width: 2px; background: var(--white); }
  .nutrition-band { position: absolute; left: 20px; width: 312px; height: 46px; background: var(--bar-fill); }

  .best-before {
    position: absolute; left: 213px; top: 1896px; width: 357px; height: 148px;
    background: var(--white); padding: 12px 14px;
    font-size: 27px; color: #000;
  }
</style>
</head>
<body>
<main class="canvas">
  <div class="wrapper-frame"></div>
  <div class="wrapper-panel"></div>

  <h1 class="brand-name">Corano</h1>

  <div class="product-visual" role="img" aria-label="Dark chocolate piece embossed with the brand name"></div>

  <p class="copy copy-intro">Lorem ipsum dolor sit amet, consectetuer adipiscing elit. Mauris tempus diam. Praesent lacus. Praesent aliquet, neque pretium congue mattis, ipsum augue dignissim ante, ac pretium nisl lectus at magna. Curabitur lorem risus, sagittis vitae, accumsan a, iaculis id, metus. Aenean ultrices turpis. Curabitur risus urna, placerat et, luctus pulvinar, auctor vel, orci. Morbi turpis arcu, egestas congue, condimentum quis, tristique cursus, leo. Praesent scelerisque. Vestibulum ante ipsum primis in faucibus orci luctus et ultrices posuere cubilia Curae; Vivamus eu orci. Phasellus lacinia iaculis mi. Curabitur lorem risus, sagittis vitae, accumsan a, iaculis id, metus. Cras facilisis felis sit amet lorem. Phasellus hendrerit. Suspendisse viverra placerat tortor. Mauris et dolor.</p>

  <p class="copy copy-wide">Lorem ipsum dolor sit amet, consectetuer adipiscing elit. Mauris tempus diam. Praesent lacus. Praesent aliquet, neque pretium congue mattis, ipsum augue dignissim ante, ac pretium nisl lectus at magna. Curabitur lorem risus, sagittis vitae, accumsan a, iaculis id, metus. Aenean ultrices turpis. Curabitur risus urna, placerat et, luctus pulvinar, auctor vel, orci. Morbi turpis arcu, egestas congue, condimentum quis, tristique cursus, leo. Praesent scelerisque. Vestibulum ante ipsum primis in faucibus orci luctus et ultrices posuere cubilia Curae; Vivamus eu orci. Phasellus lacinia iaculis mi. Curabitur lorem risus, sagittis vitae, accumsan a, iaculis id, metus. Cras facilisis felis sit amet lorem. Phasellus hendrerit. Suspendisse viverra placerat tortor. Mauris et dolor. Pellentesque tempor. Curabitur risus urna, placerat et, luctus pulvinar, auctor vel, orci. Proin diam augue, semper vitae, varius et, viverra id, felis. Phasellus auctor enim eget</p>

  <section class="nutrition-panel" aria-label="Nutrition Facts">
    <h2 class="nutrition-title">Nutrition Facts</h2>
    <div class="nutrition-rule"></div>
    <div class="nutrition-divider" style="top:74px;height:61px"></div>
    <div class="nutrition-band" style="top:150px"></div>
    <div class="nutrition-divider" style="top:211px;height:129px"></div>
    <div class="nutrition-band" style="top:359px"></div>
    <div class="nutrition-divider" style="top:420px;height:220px"></div>
  </section>

  <p class="copy copy-detail">Lorem ipsum dolor sit amet, consectetuer adipiscing elit. Mauris tempus diam. Praesent lacus. Praesent aliquet, neque pretium congue mattis, ipsum augue dignissim ante, ac pretium nisl lectus at magna. Curabitur lorem risus, sagittis vitae, accumsan a, iaculis id, metus. Aenean ultrices turpis. Curabitur risus urna, placerat et, luctus pulvinar, auctor vel, orci. Morbi turpis arcu, egestas congue, condimentum quis, tristique cursus, leo. Praesent scelerisque. Vestibulum ante ipsum primis in faucibus orci luctus et ultrices posuere cubilia Curae; Vivamus eu orci. Phasellus lacinia iaculis mi. Curabitur lorem risus, sagittis vitae, accumsan a, iaculis id, metus. Cras facilisis felis sit amet lorem. Phasellus hendrerit. Suspendisse viverra placerat tortor. Mauris et dolor. Pellentesque tempor. Curabitur risus urna, placerat et, luctus pulvinar, auctor vel, orci. Proin diam augue, semper vitae, varius et, viverra id, felis. Phasellus auctor enim eget sem.</p>

  <div class="best-before">Best before:</div>
</main>
</body>
</html>
```